Developer needs a Software blog Design

I need a design for my software blog (I'm a developer). The design should include a homepage for browser and for mobile.

Following is a wireframe: https://sketchgrid.io/kTmwqe.

The sidebar can also include my picture I you think it should.

In the mobile version the about me and subscribe with email should be popup or dropdown.

I'm currently using this: http://valpirek.quillhost.io/ which I like, but doesn't have all the component I want on the sidebar and I want something unique.

The most importnant is simple, clean and responsive.

Designs that I like:
http://blog.tarvuso.com/
http://xwrp.net/layoutbazaar/?theme=fels
http://demo.layoutvireo.com/#singularly

Out come should be a psd file with homepage and mobile homepage (and dropdowns variation for the mobile).

Target Market(s)

developers

Industry/Entity Type

Software

Font styles to use
Sans Serif

Requirements
Must have
• clean and simple. responsive. main post area need to be wide enough.

```html
<!DOCTYPE html>
<html lang="en">
<head>
<meta charset="utf-8">
<title>Valpirek – Token-Based PubSub</title>
<link href="https://fonts.googleapis.com/css2?family=Open+Sans:wght@300;400;600;700;800&family=Source+Code+Pro:wght@400&display=swap" rel="stylesheet">
<style>
:root{
  --bg-dark:#333a48;
  --field-dark:#252b36;
  --field-border:#1c212a;
  --text-light:#ffffff;
  --text-muted:#9aa1ad;
  --text-soft:#c9ced6;
  --rule-dark:#454c5a;
  --panel:#ffffff;
  --ink:#333333;
  --ink-soft:#555555;
  --ghost:#e6e6e6;
  --rule-light:#e3e3e3;
  --code-bg:#f5f5f5;
  --code-red:#d8352a;
  --code-blue:#2a7ab0;
  --chirper:#2e9fd6;
  --rss:#f0a830;
  --pagebook:#3b5a9a;
  --orbit:#dd4b39;
}
*{box-sizing:border-box;margin:0;padding:0}
html,body{width:1090px;height:1200px;overflow:hidden}
body{background:var(--bg-dark);font-family:'Open Sans',sans-serif;position:relative;color:var(--ink)}
.abs{position:absolute}

/* sidebar */
.sidebar{position:absolute;left:0;top:0;width:382px;height:1200px}
.brand{right:41px;top:46px;font-size:27px;font-weight:700;color:var(--text-light);letter-spacing:-0.5px}
.field{left:90px;width:251px;height:31px;background:var(--field-dark);border:1px solid var(--field-border);border-radius:3px;box-shadow:0 1px 0 rgba(255,255,255,.06);color:var(--text-muted);font-size:10px;padding:8px 13px}
.field svg{position:absolute;right:11px;top:8px}
.side-head{right:41px;font-size:14px;font-weight:700;color:var(--text-light);text-transform:uppercase}
.side-note{right:41px;font-size:10px;color:var(--text-muted)}
.follow{top:301px;display:flex;align-items:center}
.follow .dot{width:50px;height:50px;border-radius:50%}
.follow .lbl{margin-left:10px;line-height:1.35}
.follow .lbl small{display:block;font-size:10px;color:var(--text-light)}
.follow .lbl b{font-size:14px;font-weight:600}
.rule{height:1px;background:var(--rule-dark)}
.post{right:41px;width:240px;text-align:right}
.post h4{font-size:12.5px;font-weight:400;color:var(--text-soft);padding-right:14px;position:relative;white-space:nowrap}
.post h4::after{content:"";position:absolute;right:0;top:6px;width:8px;height:8px;border-radius:50%;background:#8d939e}
.post p{font-size:10px;color:var(--text-muted);margin:7px 20px 0 0}
.post .meta{font-size:7.5px;color:var(--text-muted);margin:9px 20px 0 0;display:flex;justify-content:flex-end;gap:12px;align-items:center}
.meta i{display:inline-block;width:9px;height:8px;border:1px solid #8d939e;border-radius:2px;margin-right:4px;vertical-align:-1px}
.links{left:210px;width:131px}
.links a{display:flex;justify-content:flex-end;align-items:center;gap:10px;height:33.5px;border-bottom:1px solid var(--rule-dark);color:var(--text-muted);font-size:10.5px;text-decoration:none}
.links a span.ic{width:11px;height:11px;border-radius:2px;background:#8d939e}
.about{left:92px;top:980px;width:145px;text-align:right;font-size:9.5px;line-height:18.7px;color:var(--text-muted)}
.portrait{left:252px;top:978px;width:88px;height:88px;border-radius:50%;background:radial-gradient(circle at 50% 40%,#8a7a70,#3a3530 60%,#22252c)}
.copy{right:41px;top:1120px;text-align:right;font-size:10px;line-height:19px;color:var(--text-muted)}

/* main panel */
.panel{position:absolute;left:382px;top:0;width:619px;height:1200px;background:var(--panel);box-shadow:0 0 8px rgba(0,0,0,.2)}
.ghost{left:28px;top:36px;font-size:58px;font-weight:800;color:var(--ghost);letter-spacing:-2px}
.tagline{left:27px;top:102px;font-size:35px;font-weight:300;color:#666}
.head-rule{left:29px;top:168px;width:561px;height:2px;background:var(--rule-light)}
.post-head{left:29px;top:172px;width:561px;height:103px;background:linear-gradient(#fff 60%,#f7f7f7);border-bottom:1px solid var(--rule-light)}
.post-title{left:45px;top:197px;font-size:25px;font-weight:400;color:var(--ink)}
.post-meta{left:47px;top:241px;display:flex;gap:20px;font-size:11px;color:#999;align-items:center}
.post-meta i{display:inline-block;width:12px;height:11px;background:#c2c2c2;border-radius:2px;margin-right:6px;vertical-align:-1px}
.body-text{left:39px;width:545px;font-size:10.2px;line-height:20.3px;color:var(--ink-soft)}
.code{left:29px;top:486px;width:561px;height:284px;background:var(--code-bg);border:1px solid var(--rule-light);border-radius:2px;font-family:'Source Code Pro',monospace;font-size:10px;color:#444}
.code div{position:absolute;white-space:pre}
.code .sp{letter-spacing:2.6px}
.code .br{font-family:'Open Sans',sans-serif;font-size:18px;font-weight:300;color:#555}
.kw{color:var(--code-red)}
.st{color:var(--code-blue)}
.share{top:858px;height:36px;width:120px;color:#fff;font-size:12px;display:flex;align-items:center;justify-content:center;gap:7px;border-radius:2px 2px 0 0}
.share span{width:11px;height:11px;border-radius:50%;background:rgba(255,255,255,.85)}
.comments{left:29px;top:893px;width:561px;height:260px;border:1px solid var(--rule-light);border-radius:2px}
.comments h3{position:absolute;left:29px;top:22px;font-size:21px;font-weight:300;color:#666}
.comments ul{position:absolute;left:24px;top:64px;list-style:none}
.comments li{font-size:10px;color:var(--ink-soft);height:25.3px;display:flex;align-items:center}
.comments li::before{content:"";width:7px;height:7px;border:1px solid #ccc;border-radius:50%;margin-right:11px}
</style>
</head>
<body>
<aside class="sidebar">
  <div class="abs brand">Valpirek</div>

  <div class="abs field" style="top:117px">Search :
    <svg width="14" height="14" viewBox="0 0 14 14"><circle cx="5.5" cy="5.5" r="4.3" fill="none" stroke="#8d939e" stroke-width="1.8"/><line x1="8.7" y1="8.7" x2="13" y2="13" stroke="#8d939e" stroke-width="2"/></svg>
  </div>

  <div class="abs side-head" style="top:181px">Newsletter Signup</div>
  <div class="abs side-note" style="top:210px">Get our recent updates through your email id :</div>
  <div class="abs field" style="top:241px;padding-left:15px">Enter your email id :
    <svg width="13" height="12" viewBox="0 0 13 12"><path d="M1 6h10M7 2l4 4-4 4" fill="none" stroke="#8d939e" stroke-width="1.5"/></svg>
  </div>

  <div class="abs follow" style="left:90px">
    <div class="dot" style="background:var(--chirper)"></div>
    <div class="lbl"><small>Follow us on</small><b style="color:var(--chirper)">Chirper</b></div>
  </div>
  <div class="abs follow" style="left:221px">
    <div class="dot" style="background:var(--rss)"></div>
    <div class="lbl"><small>Subscribe via</small><b style="color:var(--rss)">RSS</b></div>
  </div>

  <div class="abs side-head" style="top:381px">Recent Posts</div>
  <div class="abs rule" style="left:90px;top:416px;width:251px"></div>

  <div class="abs post" style="top:435px"><h4>Es simplemente el texto de relleno de</h4><p>es simplemente el texto de relleno de las...</p><div class="meta"><span><i></i>120 Comments</span><span><i></i>22 November 2014</span><span><i></i>Share</span></div></div>
  <div class="abs post" style="top:517px"><h4>Es simplemente el texto de relleno de</h4><p>es simplemente el texto de relleno de las...</p><div class="meta"><span><i></i>120 Comments</span><span><i></i>22 November 2014</span><span><i></i>Share</span></div></div>
  <div class="abs post" style="top:599px"><h4>Es simplemente el texto de relleno de</h4><p>es simplemente el texto de relleno de las...</p><div class="meta"><span><i></i>120 Comments</span><span><i></i>22 November 2014</span><span><i></i>Share</span></div></div>
  <div class="abs post" style="top:681px"><h4>Es simplemente el texto de relleno de</h4><p>es simplemente el texto de relleno de las...</p><div class="meta"><span><i></i>120 Comments</span><span><i></i>22 November 2014</span><span><i></i>Share</span></div></div>

  <nav class="abs links" style="top:760px">
    <a href="#">Codeyard <span class="ic"></span></a>
    <a href="#">Chirper <span class="ic"></span></a>
    <a href="#">Workring <span class="ic"></span></a>
    <a href="#">Contact me
      <svg width="11" height="11" viewBox="0 0 11 11"><path d="M2 1l2 0 1 3-1.3 1a6 6 0 0 0 2.3 2.3L7 6l3 1v2c0 1-1 1-1 1C5 10 1 6 1 2c0 0 0-1 1-1z" fill="#8d939e"/></svg></a>
  </nav>

  <div class="abs side-head" style="top:926px;right:44px">About Me</div>
  <div class="abs rule" style="left:90px;top:961px;width:251px"></div>
  <p class="abs about">Es simplemente el texto de relleno de las imprentas y archivos de texto. Lorem Ipsum ha sido el texto de relleno estándar de las industrias desde...</p>
  <div class="abs portrait" role="img" aria-label="Portrait photo of the blog author"></div>

  <p class="abs copy">Copyright Valpirek © 2014 •<br>All rights reserved.</p>
</aside>

<main class="panel">
  <div class="abs ghost">Valpirek</div>
  <div class="abs tagline">Es simplemente el texto de relleno...</div>
  <div class="abs post-head"></div>
  <div class="abs head-rule"></div>
  <h1 class="abs post-title">Token-Based PubSub</h1>
  <div class="abs post-meta"><span><i></i>18 days ago</span><span><i></i>DotQuor · PubSub</span><span><i></i>Share</span></div>

  <p class="abs body-text" style="top:290px">I recently pushed two new features to both QuorMQ and DotQuor: manual subscriptions and welcome message, both for the XPub socket. In this post, I will explore what we can do with the manual subscriptions feature. The next post will cover the welcome message.</p>
  <p class="abs body-text" style="top:371px">Neither feature is part of any release of QuorMQ or DotQuor yet, so you will have to compile from the source code to use the new features.</p>
  <p class="abs body-text" style="top:432px">I will use DotQuor throughout the post, but you can implement the examples using any QuorMQ binding.</p>

  <div class="abs code">
    <div style="left:32px;top:25px"><span class="kw">using</span> (<span class="kw">var</span> context = DotQuorContext.Create())</div>
    <div class="br" style="left:32px;top:46px">{</div>
    <div class="sp" style="left:52px;top:66px">string[] topics = new string[] { <span class="st">"A"</span>, <span class="st">"B"</span>, <span class="st">"C"</span> };</div>
    <div class="sp" style="left:63px;top:86px">Random random = <span class="kw">new</span> Random();</div>
    <div class="br" style="left:403px;top:90px">}</div>
    <div style="left:32px;top:126px"><span class="kw">using</span> (<span class="kw">var</span> context = DotQuorContext.Create())</div>
    <div style="left:32px;top:149px;color:#222">// we only handle subscription requests, unsubscription and any</div>
    <div style="left:32px;top:169px;color:#222">// other type of messages will be dropped</div>
    <div class="br" style="left:32px;top:193px">{</div>
    <div class="sp" style="left:52px;top:214px">string[] topics = new string[] { <span class="st">"A"</span>, <span class="st">"B"</span>, <span class="st">"C"</span> };</div>
    <div class="sp" style="left:63px;top:234px">Random random = <span class="kw">new</span> Random();</div>
    <div class="br" style="left:403px;top:238px">}</div>
  </div>

  <p class="abs body-text" style="top:789px">As noted in the example, we confirm all subscription requests, but we drop any other type of request. The subscriber will not be able to unsubscribe.</p>

  <div class="abs share" style="left:37px;background:var(--chirper)"><span></span>Chirper</div>
  <div class="abs share" style="left:159px;background:var(--pagebook)"><span></span>Pagebook</div>
  <div class="abs share" style="left:280px;background:var(--orbit)"><span></span>Orbit Plus</div>

  <section class="abs comments">
    <h3>Comments ( 15 )</h3>
    <ul>
      <li>As noted in the example, we confirm all subscription requests, but we drop any other.</li>
      <li>Es simplemente el texto de relleno de las imprentas y archivos de texto.</li>
      <li>desconocido usó una galería de textos y los mezcló de tal manera que logró hacer.</li>
      <li>Al contrario del pensamiento popular, el texto de Lorem Ipsum no es simplemente texto aleatorio.</li>
      <li>Tiene sus raices en una pieza clásica de la literatura del Latin, que data del año 45 antes.</li>
      <li>As noted in the example, we confirm all subscription requests, but we drop any other...</li>
      <li>As noted in the example, we confirm all subscription requests.</li>
    </ul>
  </section>
</main>
</body>
</html>
```